Briefpapier für Betrieb aus der Landwirtschaft
Zielgruppe
der Firmen name ist Brandol Jürgen
Wir sind ein Betrieb der aus der Landwirtschaft kommt und sich auf die bewirtschaftung von Streuobstäckern und wiesen spezialisiert hat.
Die Früchte der Bäume werden über eine von uns mitgegründete Genossenschaft vertrieben... Andere Früchte werden an destilierien und an Endverbraucher verkauft.
Zielgruppe:
Das Breifpapier soll für geschäftsbriefe rechnungen Lieferscheine, auftragsbestätigungen verwendung finden.
Und an Endkunden, Lieferanten und Geschaftspartner gehen !!
Wir haben ein Biolabel gegründet wiesel pur terra eventuell kann man sich an dem Logo orientieren !!
Aufgabenstellung
Ich habe unseren alten Briefbogen angehängt !!! Bitte nicht kopieren oder optimieren !!! Er ist nur da um die Daten zu nehmen !!! Briefpapier soll kompl. neu desingt werden... Firmen Name Brandol Jürgen
Ich brauche platz für die Biosiegel 2 in der Zahl
Frech / Modern eventuell mit wasserzeichen , hohen wiedererkennungswert.
Nach abschluss des desingns sollen Visitenkarten gemacht werden

```html
<!DOCTYPE html>
<html lang="de">
<head>
<meta charset="utf-8">
<title>Briefpapier Brandol Jürgen</title>
<link href="https://fonts.googleapis.com/css2?family=Montserrat:wght@400;500;600;700&family=Arimo:wght@400;700&display=swap" rel="stylesheet">
<style>
  :root {
    --backdrop: #e6e6e6;
    --paper: #ffffff;
    --green-dark: #0f6a34;
    --green-mid: #3f8f2f;
    --green-light: #93c223;
    --watermark-a: #eef5e0;
    --watermark-b: #dce9df;
    --ink: #4a4a4a;
    --body-ink: #1c1c1c;
  }
  * { box-sizing: border-box; margin: 0; padding: 0; }
  html, body { width: 1200px; height: 720px; overflow: hidden; }
  body {
    background: var(--backdrop);
    position: relative;
    font-family: "Montserrat", sans-serif;
  }
  .sheet {
    position: absolute;
    top: 48px;
    width: 430px;
    height: 609px;
    background: var(--paper);
    overflow: hidden;
  }
  .sheet--blank { left: 113px; }
  .sheet--letter { left: 668px; }

  .top-bar {
    position: absolute; left: 0; top: 0; width: 100%; height: 11px;
    background: linear-gradient(90deg, var(--green-dark), var(--green-light));
  }
  .bottom-bar {
    position: absolute; left: 0; bottom: 0; width: 100%; height: 18px;
    background: linear-gradient(90deg, var(--green-light), var(--green-mid) 70%, var(--green-dark));
  }
  .watermark-area {
    position: absolute; left: 0; top: 36px; width: 430px; height: 555px;
  }
  .label-tab {
    position: absolute; left: 302px; top: 0; width: 108px; height: 110px;
    background: linear-gradient(180deg, var(--green-mid), var(--green-light));
    border-radius: 0 0 10px 10px;
    color: #fff;
    padding: 28px 0 0 10px;
  }
  .label-tab__seal {
    font-weight: 700; font-size: 11.5px; line-height: 11px; letter-spacing: 0.2px;
  }
  .label-tab__brand {
    margin-top: 24px; font-weight: 700; font-size: 16px; letter-spacing: 0.5px;
  }
  .brand-head {
    position: absolute; left: 48px; top: 45px;
    display: flex; align-items: center; gap: 6px;
  }
  .brand-head__dot {
    width: 19px; height: 19px; border-radius: 50%; background: var(--green-mid);
  }
  .brand-head__name {
    font-weight: 600; font-size: 18.5px; color: var(--ink); letter-spacing: 0.4px;
  }
  .sender-line {
    position: absolute; left: 48px; top: 97px;
    font-size: 3.6px; font-weight: 500; color: var(--ink);
  }
  .recipient {
    position: absolute; left: 49px; top: 110px;
    font-family: "Arimo", sans-serif; font-size: 7.8px; line-height: 8.8px; color: var(--body-ink);
  }
  .subject {
    position: absolute; left: 49px; top: 238px;
    font-family: "Arimo", sans-serif; font-weight: 700; font-size: 7.6px; color: var(--body-ink);
  }
  .letter-body {
    position: absolute; left: 49px; top: 266px; width: 330px;
    font-family: "Arimo", sans-serif; font-size: 7.4px; line-height: 9.55px; color: var(--body-ink);
    text-align: justify; hyphens: auto;
  }
  .letter-body .salutation { margin-bottom: 9.5px; }
  .footer {
    position: absolute; left: 0; top: 554px; width: 100%; height: 36px;
    font-size: 5.5px; line-height: 6.6px; color: var(--ink);
  }
  .footer__col {
    position: absolute; top: 0; height: 36px;
    border-left: 1px solid var(--green-light);
    padding: 4px 0 0 4px;
  }
  .footer__col--person { left: 46px; }
  .footer__col--contact { left: 158px; }
  .footer__col--bank { left: 295px; }
  .footer__gap { height: 4px; }
</style>
</head>
<body>

  <section class="sheet sheet--blank" aria-label="Briefbogen ohne Text">
    <div class="top-bar"></div>
    <svg class="watermark-area" viewBox="0 0 430 555" role="img" aria-label="Großes, zartgrünes Wasserzeichen des Betriebs">
      <defs>
        <linearGradient id="wm1" x1="0" y1="0" x2="1" y2="1">
          <stop offset="0" stop-color="#eef5e0"/>
          <stop offset="1" stop-color="#dce9df"/>
        </linearGradient>
      </defs>
      <rect x="0" y="0" width="430" height="555" fill="url(#wm1)" opacity="0.55"/>
    </svg>
    <div class="label-tab">
      <div class="label-tab__seal">WIESEL PUR<br>TERRA</div>
      <div class="label-tab__brand">FELVARO</div>
    </div>
    <div class="brand-head">
      <span class="brand-head__dot"></span>
      <span class="brand-head__name">BRANDOL JÜRGEN</span>
    </div>
    <div class="sender-line">Jürgen Brandol . Lindenweg 12 . 97811 Hollbach OT Kernau</div>
    <footer class="footer">
      <div class="footer__col footer__col--person">Jürgen Brandol<div class="footer__gap"></div>Lindenweg 12<br>97811 Hollbach<br>OT Kernau</div>
      <div class="footer__col footer__col--contact">Fon +49 (0)9361 4820517<br>Fax +49 (0)9361 482059<div class="footer__gap"></div>kontakt@juergenbrandol.de<br>www.juergenbrandol.de</div>
      <div class="footer__col footer__col--bank">SteuerNr.: 218/604/33915<div class="footer__gap"></div>Bank Talbank Mainfranken<br>IBAN DE71790500007302118846<br>BIC TLBKDEF1XXX</div>
    </footer>
    <div class="bottom-bar"></div>
  </section>

  <section class="sheet sheet--letter" aria-label="Briefbogen mit Mustertext">
    <div class="top-bar"></div>
    <svg class="watermark-area" viewBox="0 0 430 555" role="img" aria-label="Großes, zartgrünes Wasserzeichen des Betriebs">
      <defs>
        <linearGradient id="wm2" x1="0" y1="0" x2="1" y2="1">
          <stop offset="0" stop-color="#eef5e0"/>
          <stop offset="1" stop-color="#dce9df"/>
        </linearGradient>
      </defs>
      <rect x="0" y="0" width="430" height="555" fill="url(#wm2)" opacity="0.55"/>
    </svg>
    <div class="label-tab">
      <div class="label-tab__seal">WIESEL PUR<br>TERRA</div>
      <div class="label-tab__brand">FELVARO</div>
    </div>
    <div class="brand-head">
      <span class="brand-head__dot"></span>
      <span class="brand-head__name">BRANDOL JÜRGEN</span>
    </div>
    <div class="sender-line">Jürgen Brandol . Lindenweg 12 . 97811 Hollbach OT Kernau</div>
    <address class="recipient" style="font-style:normal">Firma<br>Herrn Max Mustermann<br>Straße Hausnummer<br>PLZ Ort</address>
    <div class="subject">Betreffszeile</div>
    <div class="letter-body">
      <p class="salutation">Sehr geehrter Herr Mustermann,</p>
      <p>Iciuntur minctat reritas inctotae cusa quam, ut hillatemo incti simus sum ipiciliquia simi, nus quam aditatur mollitiatur?</p>
      <p>Ihit evenihillam, venimi, sumquid itaturiae plat quis con nis nem es volo que net pos nusci cum voluptur archilligent labor sumqui represtemo cum fugitat ibuscimusam erferum se natur?</p>
      <p>Ovitas ut porendigente nullabore, et mod eni te enest liciis quam si sunt, sam, cum ullias millorrumque dollatet que venda et ut volores erspici enduscias ma pos ut quiditiam ape nos doluptatur sae de aut essi digenis aut quodicia aut facestia quaepe sum volore net fugita culpa quae nis reperum quo mos num es dio. Et magnist volorerupis es atatem int assit quam rempele ssimoluptio velit, qui cum rate dolore ducipsa nisqui consed modit libus, totat parum, ius et eatem labo. Neque acea quassequi dolestr uptatist, si as quassit ectotatis dolor suntem re sinctiur? Oreperferae. Et arcidusda nia nam lantur am ipient voluptaquam volorio maxim quatatur, te non rest et qui id et occati nonsecea volorposant.</p>
      <p>Aximill estemque eos nonsentint apitem. Unda aliatus dignitatem la voluptat.</p>
      <p>Nemolum as ea dolorest fugia venes comnitam, totae. Tatur assequae consequiae ex elenihil modis a comnim duciend untibus, atende illabo. Fugianto culparc hillorp orerspe rsperibus maximin istentiatis endist, utatatur?</p>
      <p>Aximodio. Itates auditibus, iducima quis alit eaque venist quatque plaborem autatio mi, quod quatumquatur sita cumqui te ne nos apicit explignis sitam, nostrum eatia vel etum, sam reriam eiur antem quod qui que voluptatem rat porerias dolore iliaturio officab oratiae rem. Ad que nulloreiunt.</p>
      <p>Hendit, expel mi, sit lacest ella voluptas dolorer ciligent lab ium quo.</p>
      <p>Nat. Nobis volorrores idis duci doluptae asint.</p>
    </div>
    <footer class="footer">
      <div class="footer__col footer__col--person">Jürgen Brandol<div class="footer__gap"></div>Lindenweg 12<br>97811 Hollbach<br>OT Kernau</div>
      <div class="footer__col footer__col--contact">Fon +49 (0)9361 4820517<br>Fax +49 (0)9361 482059<div class="footer__gap"></div>kontakt@juergenbrandol.de<br>www.juergenbrandol.de</div>
      <div class="footer__col footer__col--bank">SteuerNr.: 218/604/33915<div class="footer__gap"></div>Bank Talbank Mainfranken<br>IBAN DE71790500007302118846<br>BIC TLBKDEF1XXX</div>
    </footer>
    <div class="bottom-bar"></div>
  </section>

</body>
</html>
```